Brand Identity Stationary Package

Hello I'm looking for a full branding package for my Property Management Company. I have a logo but looking to have the following
Business Card
Email signature
Facebook cover photo
Letterhead (word.doc)
#10 Envelope
Pocket Folder - link to 9x12 pocket folder design specs https://www.plorafine.ca/marketing-materials/presentation-folders
would like everything to match and be brand identifiable. The company looks after residential properties/apartments and some commercial properties. Attached is a zip of the files.
For Business Card
Name: Gideon Falkner
Position: Operations Manager
Number: 1 (506) 384-2917
Email: Gideon@quarrytide.ca
Website: Quarrytide.ca
Property Management

```html
<!DOCTYPE html>
<html lang="en">
<head>
<meta charset="utf-8">
<title>Quarrytide Stationery Set</title>
<link rel="stylesheet" href="https://fonts.googleapis.com/css2?family=Montserrat:wght@600&family=Open+Sans:wght@400;600&display=swap">
<style>
:root{
  --bg:#ececec;
  --paper:#f8f8f8;
  --ink:#1c1c1c;
  --text:#555;
  --green:#7aa63a;
  --white:#ffffff;
  --faint:#e9e9e9;
}
*{box-sizing:border-box;margin:0;padding:0}
html,body{width:1181px;height:1200px;overflow:hidden}
body{background:var(--bg);position:relative;font-family:"Open Sans",sans-serif;color:var(--text)}
.piece{position:absolute;box-shadow:0 3px 10px rgba(0,0,0,.12)}
.brand{font-family:"Montserrat",sans-serif;font-weight:600;letter-spacing:.04em;color:var(--ink);white-space:nowrap}
.on-dark .brand{color:var(--white)}
.green-rule{position:absolute;left:0;right:0;bottom:0;background:var(--green)}
.web{font-size:9px;color:var(--white)}
.web span{color:var(--green)}

/* letterhead */
.letterhead{left:288px;top:98px;width:288px;height:408px;background:var(--paper)}
.letterhead .brand{position:absolute;left:31px;top:34px;font-size:13px}
.contact{position:absolute;font-size:5px;line-height:7px;color:var(--text)}
.letterhead .contact{left:191px;top:26px}
.contact svg{width:5px;height:5px;vertical-align:-1px;margin-right:2px;fill:var(--green)}
.letter-body{position:absolute;left:31px;top:104px;width:230px;font-size:4.6px;line-height:7.4px;color:#666}
.letter-body p{margin-bottom:7.5px;text-align:justify}
.signature{position:absolute;left:32px;top:302px;width:32px;height:30px}
.letterhead .green-rule{height:3px}

/* folder cover */
.folder-cover{left:626px;top:79px;width:340px;height:429px;background:var(--ink)}
.folder-cover .brand{position:absolute;left:0;right:0;top:190px;text-align:center;font-size:30px}
.folder-cover .web{position:absolute;left:0;right:0;top:392px;text-align:center;font-size:10px}

/* cards */
.card-front{left:184px;top:542px;width:130px;height:73px;background:var(--ink)}
.card-front .brand{position:absolute;left:0;right:0;top:26px;text-align:center;font-size:12px}
.card-front .web{position:absolute;left:0;right:0;top:57px;text-align:center;font-size:4.5px}
.card-back{left:184px;top:636px;width:130px;height:73px;background:var(--paper)}
.card-back .brand{position:absolute;left:11px;top:30px;font-size:8.5px}
.card-back .divider{position:absolute;left:67px;top:20px;width:1px;height:35px;background:var(--green)}
.card-back .contact{left:72px;top:20px;font-size:3.6px;line-height:5px}
.card-back .name{color:var(--green);font-weight:600;font-size:4.4px}
.card-back .green-rule{height:2px}

/* envelope front */
.envelope-front{left:348px;top:553px;width:322px;height:153px;background:var(--paper)}
.envelope-front .panel{position:absolute;right:0;top:5px;width:112px;height:143px;background:var(--faint)}
.envelope-front .brand{position:absolute;left:21px;top:20px;font-size:13px}
.envelope-front .address{position:absolute;left:21px;top:42px;width:95px;text-align:center;font-size:6px;line-height:7.5px;color:#444}
.envelope-front .green-rule{height:3px}

/* envelope back */
.envelope-back{left:702px;top:553px;width:322px;height:153px;background:var(--paper)}
.envelope-back svg{position:absolute;left:0;top:0}
.envelope-back .brand{position:absolute;left:0;right:0;top:16px;padding-left:60px;text-align:center;font-size:11px;color:var(--white)}

/* folder outside spread */
.folder-outside{left:40px;top:820px;width:520px;height:320px;background:var(--ink)}
.folder-outside .fold{position:absolute;left:260px;top:0;width:1px;height:100%;background:#333}
.folder-outside .brand{position:absolute;left:260px;width:260px;top:128px;text-align:center;font-size:20px;color:var(--white)}
.folder-outside .web{position:absolute;left:260px;width:260px;top:286px;text-align:center;font-size:7px}
.folder-outside .contact{left:26px;top:268px;color:#ddd;font-size:5px;line-height:7px}
.folder-outside .contact b{color:var(--green);font-weight:600}
.folder-outside .green-rule{height:3px}

/* folder inside spread */
.folder-inside{left:620px;top:820px;width:520px;height:320px;background:var(--paper)}
.folder-inside .fold{position:absolute;left:260px;top:0;width:1px;height:100%;background:#ddd}
.pocket{position:absolute;bottom:0;height:104px;background:var(--green)}
.pocket.left{left:0;width:257px;border-top-right-radius:10px}
.pocket.right{left:263px;width:257px;border-top-left-radius:10px}
.slot-card{position:absolute;left:340px;top:228px;width:92px;height:50px;background:var(--paper);box-shadow:0 1px 4px rgba(0,0,0,.2)}
.slot-card .brand{position:absolute;left:7px;top:22px;font-size:6px}
.slot-card .divider{position:absolute;left:48px;top:13px;width:1px;height:24px;background:var(--green)}
.slot-card .contact{left:52px;top:13px;font-size:2.8px;line-height:3.8px}
</style>
</head>
<body>

<section class="piece letterhead">
  <div class="brand">QUARRYTIDE</div>
  <div class="contact">
    14 Lark Hollow Road,<br>Brookmere, ON K7R 3P1<br>
    <svg viewBox="0 0 10 10"><path d="M2 1l2 0 1 2-1 1c1 2 2 3 3 3l1-1 2 1 0 2c-5 0-9-4-8-8z"/></svg>1 (506) 384-2917<br>
    <svg viewBox="0 0 10 10"><rect x="0" y="2" width="10" height="6"/></svg>Gideon@quarrytide.ca<br>
    <svg viewBox="0 0 10 10"><circle cx="5" cy="5" r="4.5"/></svg>www.quarrytide.ca
  </div>
  <div class="letter-body">
    <p style="margin-bottom:8px">Dear customer,</p>
    <p>Lorem ipsum dolor sit amet, consectetur adipisicing elit, sed do eiusmod tempor incididunt ut labore et dolore magna aliqua. Ut enim ad minim veniam, quis nostrud exercitation ullamco laboris nisi ut aliquip ex ea commodo consequat. Duis aute irure dolor in reprehenderit in voluptate velit esse cillum dolore eu fugiat nulla pariatur. Excepteur sint occaecat cupidatat non proident, sunt in culpa qui officia deserunt mollit anim id est laborum.</p>
    <p>Lorem ipsum dolor sit amet, consectetur adipisicing elit, sed do eiusmod tempor incididunt ut labore et dolore magna aliqua. Ut enim ad minim veniam, quis nostrud exercitation ullamco laboris nisi ut aliquip ex ea commodo consequat. Duis aute irure dolor in reprehenderit in voluptate velit esse cillum dolore eu fugiat nulla pariatur. Excepteur sint occaecat cupidatat non proident, sunt in culpa qui officia deserunt mollit anim id est laborum.</p>
    <p>Lorem ipsum dolor sit amet, consectetur adipisicing elit, sed do eiusmod tempor incididunt ut labore et dolore magna aliqua. Ut enim ad minim veniam, quis nostrud exercitation ullamco laboris nisi ut aliquip ex ea commodo consequat. Duis aute irure dolor in reprehenderit in voluptate velit esse cillum dolore eu fugiat nulla pariatur. Excepteur sint occaecat cupidatat non proident, sunt in culpa qui officia deserunt mollit anim id est laborum.</p>
    <p>Lorem ipsum dolor sit amet, consectetur adipisicing elit, sed do eiusmod tempor incididunt ut labore et dolore magna aliqua. Ut enim ad minim veniam, quis nostrud exercitation ullamco laboris nisi ut aliquip ex ea commodo consequat. Duis aute irure dolor in reprehenderit.</p>
    <p>Yours Sincerely,</p>
  </div>
  <div class="signature" role="img" aria-label="Handwritten signature" style="background:linear-gradient(135deg,transparent 45%,#bbb 50%,transparent 55%)"></div>
  <div class="green-rule"></div>
</section>

<section class="piece folder-cover on-dark">
  <div class="brand">QUARRYTIDE</div>
  <div class="web">www.<span>quarrytide</span>.ca</div>
</section>

<section class="piece card-front on-dark">
  <div class="brand">QUARRYTIDE</div>
  <div class="web">www.<span>quarrytide</span>.ca</div>
</section>

<section class="piece card-back">
  <div class="brand">QUARRYTIDE</div>
  <div class="divider"></div>
  <div class="contact">
    <span class="name">GIDEON FALKNER</span><br>
    Operations Manager<br>
    14 Lark Hollow Road,<br>Brookmere, ON K7R 3P1<br>
    1 (506) 384-2917<br>
    Gideon@quarrytide.ca<br>
    www.quarrytide.ca
  </div>
  <div class="green-rule"></div>
</section>

<section class="piece envelope-front">
  <div class="panel"></div>
  <div class="brand">QUARRYTIDE</div>
  <div class="address">Unit 8 / 61 Harbourline Way,<br>Tarrin, NSW 2290</div>
  <div class="green-rule"></div>
</section>

<section class="piece envelope-back">
  <svg width="322" height="70" viewBox="0 0 322 70">
    <path d="M0 0H322L316 55Q315 60 308 60H14Q7 60 6 55Z" fill="var(--ink)"/>
  </svg>
  <div class="brand">QUARRYTIDE</div>
</section>

<section class="piece folder-outside on-dark">
  <div class="fold"></div>
  <div class="contact">
    <b>Quarrytide Ltd</b><br>
    14 Lark Hollow Road, Brookmere, ON K7R 3P1<br>
    1 (506) 384-2917 &nbsp; Gideon@quarrytide.ca<br>
    www.quarrytide.ca
  </div>
  <div class="brand">QUARRYTIDE</div>
  <div class="web">www.<span>quarrytide</span>.ca</div>
  <div class="green-rule"></div>
</section>

<section class="piece folder-inside">
  <div class="fold"></div>
  <div class="pocket left"></div>
  <div class="pocket right"></div>
  <div class="slot-card">
    <div class="brand">QUARRYTIDE</div>
    <div class="divider"></div>
    <div class="contact">
      <span style="color:var(--green)">GIDEON FALKNER</span><br>
      Operations Manager<br>
      1 (506) 384-2917<br>
      Gideon@quarrytide.ca<br>
      www.quarrytide.ca
    </div>
  </div>
</section>

</body>
</html>
```